Create New Bussiness Card For New Shoes Store

Vandrel is a store that sells a variety of skateboard shoes such as Kolvo, Frisk etc. we also sell some skateboard and all skateboard accessories.
we like black and white style logo, but also like blue as well.
We are fully assembled with a deck, truck, wheels, and bearings. Add some personality to your board with a fun, graphic skateboard deck. Constructed of thick 7 ply maple,
Target Market(s)
Target audience: 12-40 year old
especially for young man
Industry/Entity Type
Industrial
Contact Information for Business Card
Name: Vandrel
Address1: 2493 Marlow Pike Rd
City: Xenia
State: Ohio
Zip: 45385
Country: US
Phone: 614583062
email: danbrellick@quortmail.example

```html
<!DOCTYPE html>
<html lang="en">
<head>
<meta charset="utf-8">
<title>Vandrel Business Card</title>
<link href="https://fonts.googleapis.com/css2?family=Source+Sans+3:wght@300;400;600&display=swap" rel="stylesheet">
<style>
  :root {
    --backdrop: #4a3f3b;
    --card: #121212;
    --accent: #c27ccc;
    --text: #e9e9e9;
    --silver: #cfcfcf;
    --divider: #5a5a5a;
  }
  * { margin: 0; padding: 0; box-sizing: border-box; }
  html, body { width: 1200px; height: 814px; overflow: hidden; }
  body {
    background: var(--backdrop);
    font-family: "Source Sans 3", "Helvetica Neue", Arial, sans-serif;
    position: relative;
  }
  .card {
    position: absolute;
    top: 258px;
    width: 520px;
    height: 298px;
    background: var(--card);
    border-radius: 3px;
    box-shadow: 0 6px 18px rgba(0,0,0,.35);
  }
  .card--front { left: 60px; }
  .card--back { left: 620px; }

  .brand {
    position: absolute;
    display: flex;
    align-items: center;
    gap: 12px;
    font-weight: 300;
    letter-spacing: 1px;
    white-space: nowrap;
  }
  .brand__dot {
    border-radius: 50%;
    border: 2px solid currentColor;
  }
  .card--front .brand {
    left: 40px; top: 124px;
    color: var(--accent);
    font-size: 40px;
  }
  .card--front .brand__dot { width: 22px; height: 22px; }

  .divider {
    position: absolute;
    left: 262px; top: 60px;
    width: 1px; height: 178px;
    background: var(--divider);
  }
  .contact {
    position: absolute;
    left: 282px; top: 70px;
    color: var(--text);
    font-size: 15px;
    line-height: 21px;
    white-space: nowrap;
  }
  .contact__name {
    color: var(--accent);
    font-size: 21px;
    font-weight: 600;
    margin-bottom: 8px;
  }
  .contact__row {
    display: flex;
    align-items: center;
    gap: 8px;
  }
  .contact__icon { width: 13px; height: 13px; flex: none; }

  .card--back .brand {
    left: 50%; top: 100px;
    transform: translateX(-50%);
    color: var(--silver);
    font-size: 48px;
  }
  .card--back .brand__dot { width: 26px; height: 26px; }
  .card--back .url {
    position: absolute;
    left: 0; right: 0; top: 198px;
    text-align: center;
    color: var(--text);
    font-size: 14px;
  }
</style>
</head>
<body>
  <section class="card card--front">
    <div class="brand"><span class="brand__dot"></span><span class="brand__name">Vandrel</span></div>
    <div class="divider"></div>
    <div class="contact">
      <div class="contact__name">Owen Hale</div>
      <div>2493 Marlow Pike Rd</div>
      <div>Brenmoor, Ardale 40871, US</div>
      <div class="contact__row">
        <svg class="contact__icon" viewBox="0 0 16 16"><path fill="var(--accent)" d="M3 1l3 3-1.6 2a9 9 0 0 0 5.6 5.6L12 10l3 3-2 2C7 15 1 9 1 3z"/></svg>
        <span>614583062</span>
      </div>
      <div class="contact__row">
        <svg class="contact__icon" viewBox="0 0 16 16"><rect x="1" y="3" width="14" height="10" fill="var(--accent)"/><path d="M1 3l7 6 7-6" fill="none" stroke="var(--card)" stroke-width="1.5"/></svg>
        <span>hello@vandrelshop.example</span>
      </div>
      <div class="contact__row">
        <svg class="contact__icon" viewBox="0 0 16 16"><circle cx="8" cy="8" r="7" fill="var(--accent)"/><path d="M1 8h14M8 1c-3 4-3 10 0 14M8 1c3 4 3 10 0 14" fill="none" stroke="var(--card)" stroke-width="1.2"/></svg>
        <span>www.vandrelshop.example</span>
      </div>
    </div>
  </section>

  <section class="card card--back">
    <div class="brand"><span class="brand__dot"></span><span class="brand__name">Vandrel</span></div>
    <div class="url">www.vandrelshop.example</div>
  </section>
</body>
</html>
```